漫画の部分を抜くと、8ページほどの作業量です。

カラーマンガは、29日に完成してきますので、
同じマンガ家さんの完成色合いはこちら、
下記の感じで色合いで完成してきます。
https://mirukado.jp/web/tofuri/index.html#b4

詳しくは資料をみてください。
資料は下記から全てDLできます。

https://tofuri.jp/s/qxwelRmb

A5
8ページ
赤系、青系、水色系
• イラストレーター形式 (.ai)
• フォトショップ形式 (.psd)
実際の作業に関してですが、

8ページのパンフレット 1冊
1ページの両面 1枚

の合計で10ページになります。
素材集のなかに、写真を複数追加しました。
もし、良ければ使ってください。
漫画の彩色が終わりました。
もうすぐ締め切りですが、UPしておきます。
漫画のデーターは、WEB用ですが、印刷用がありますので、高画質を当選者様にはお渡しします。

他の方と違い、緊急性の出し方がうまかったです。

いつも、本当にありがとうございます。

```html
<!DOCTYPE html>
<html lang="ja">
<head>
<meta charset="utf-8">
<title>エアコン省エネ回復剤 よくあるご質問</title>
<link href="https://fonts.googleapis.com/css2?family=M+PLUS+Rounded+1c:wght@500;800&family=Noto+Sans+JP:wght@400;500;700&display=swap" rel="stylesheet">
<style>
:root{
  --paper:#fffbea;
  --title-bg:#fde3e6;
  --title-line:#f3a7b0;
  --red:#e2322f;
  --q-pink:#ee6b8e;
  --a-orange:#f39a2c;
  --q-band:#fdeef0;
  --rule:#f0b9c3;
  --ink:#3a2e2a;
  --leaf-1:#9dcd5a;
  --leaf-2:#d7ebb6;
}
*{margin:0;padding:0;box-sizing:border-box}
html,body{width:847px;height:1200px;overflow:hidden;background:#fff}
.sheet{position:relative;width:847px;height:1200px;background:var(--paper);font-family:"Noto Sans JP",sans-serif;color:var(--ink)}
.vine{position:absolute;top:0;width:70px;height:1200px;background:linear-gradient(180deg,var(--leaf-2),var(--leaf-1) 50%,var(--leaf-2))}
.vine--left{left:0;border-radius:0 40px 40px 0;opacity:.75}
.vine--right{right:0;border-radius:40px 0 0 40px;opacity:.75}
.title{position:absolute;left:205px;top:42px;width:440px;height:52px;background:var(--title-bg);border:2px solid var(--title-line);border-radius:8px;text-align:center;font-family:"M PLUS Rounded 1c",sans-serif;font-weight:800;font-size:32px;line-height:48px;color:var(--red);letter-spacing:2px}
.badge{position:absolute;left:728px;top:40px;width:88px;height:88px;border-radius:50%;background:#fff3c4;border:3px solid var(--leaf-1)}
.content{position:absolute;left:88px;top:110px;width:672px}
.section-head{font-family:"M PLUS Rounded 1c",sans-serif;font-weight:800;font-size:34px;color:var(--red);text-align:center;padding-bottom:6px;border-bottom:2px solid var(--rule);margin-bottom:10px;letter-spacing:3px}
.section-head--second{margin-top:22px}
.qa{list-style:none}
.qa li{display:flex;align-items:flex-start;gap:10px;font-size:13.5px;line-height:1.6;padding:7px 8px;border-bottom:1px dotted var(--rule)}
.qa .q{background:var(--q-band);font-weight:700}
.mark{flex:0 0 22px;height:22px;border-radius:4px;color:#fff;font-weight:700;font-size:14px;text-align:center;line-height:22px}
.q .mark{background:var(--q-pink)}
.a .mark{background:var(--a-orange)}
.brand{position:absolute;left:0;right:0;top:1150px;text-align:center;font-family:"Noto Sans JP",sans-serif;font-weight:500;font-size:22px;line-height:32px;color:var(--ink);letter-spacing:1px}
</style>
</head>
<body>
<div class="sheet">
  <div class="vine vine--left" role="img" aria-label="左側を縦に伝う緑の蔓と葉の装飾"></div>
  <div class="vine vine--right" role="img" aria-label="右側を縦に伝う緑の蔓と葉の装飾"></div>

  <h1 class="title">エアコン省エネ回復剤</h1>
  <div class="badge" role="img" aria-label="省エネ認定バッジ"></div>

  <main class="content">
    <h2 class="section-head">よくあるご質問</h2>
    <ul class="qa">
      <li class="q"><span class="mark">Q</span>施工後、効果が出るまで、どれだけ時間がかかりますか？</li>
      <li class="a"><span class="mark">A</span>エアコン回復剤を注入してから、5分程度で振動や騒音が低下します。</li>
      <li class="q"><span class="mark">Q</span>一度、施工してもらうと、どれだけ有効なんですか？</li>
      <li class="a"><span class="mark">A</span>コンプレッサーの作動回数の低減が、約5年間は持続します。（使用環境により異なります）</li>
      <li class="q"><span class="mark">Q</span>施工後、特別なメンテナンスは必要ですか？</li>
      <li class="a"><span class="mark">A</span>「金属表面修復技術」を利用しているので、エアコン自ら傷の修復を行います。<br>その為、特別なメンテナンスは必要ありません。</li>
      <li class="q"><span class="mark">Q</span>どんなエアコンでも大丈夫ですか？</li>
      <li class="a"><span class="mark">A</span>基本的には、どんなエアコンでも施工可能です。<br>最終的には、現状を確認して判断させていただき、お見積もりいたします。</li>
      <li class="q"><span class="mark">Q</span>購入して2年ほどのエアコンですが、それでも効果を期待できますか？</li>
      <li class="a"><span class="mark">A</span>新品でも、すでに傷は発生しています。<br>エアコンの寿命を延ばす効果があるので、ぜひお試しください。</li>
    </ul>

    <h2 class="section-head section-head--second">一番多い疑問点です</h2>
    <ul class="qa">
      <li class="q"><span class="mark">Q</span>省エネ回復剤を注入して壊れませんか？</li>
      <li class="a"><span class="mark">A</span>実は皆様の疑問に、コンプレッサー内部には1リットル以上のオイルが入っており、<br>適合する添加オイルのため心配はございません。</li>
      <li class="q"><span class="mark">Q</span>電気代が下がるのはなぜですか？</li>
      <li class="a"><span class="mark">A</span>コンプレッサー内部の傷が修復されることにより圧縮比率が向上することで、吹き出し温度が2〜3度下がるため、室内設定温度に早く到達するためエネルギーの消費を抑えます。<br>室外機洗浄と一緒に行うとさらに効果的です。<br>月10〜30％電気料金が下がるデータがございます。</li>
      <li class="q"><span class="mark">Q</span>何年目のエアコンが効果が期待できますか？</li>
      <li class="a"><span class="mark">A</span>統計データでは5年目以降の機器に効果が見られる場合が多いです。</li>
      <li class="q"><span class="mark">Q</span>施工実績を教えてください。</li>
      <li class="a"><span class="mark">A</span>官公庁のオフィス、大手メーカー、大手食品スーパー、コンビニ、工場他がございます。</li>
    </ul>
  </main>

  <div class="brand">Kaizenia</div>
</div>
</body>
</html>
```